Business Card Design

Very plain simple card, Plain modern font. Background. Grey fading to black. Large Bright lime green text. Saying.

Greywater

Small other details in white text.

Irish Horse Sales . Livery . Stud . Shows

Mark Dabrowski
Greywater Stud
Birch Lodge
Carrowmede Lane
Thistlecombe
Wendlowshire
QX4 7JX

Email. office@greywaterstud.co.uk
Tel. 07482 936504

Industry/Entity Type

Business

Contact Information for Business Card

As below

```html
<!DOCTYPE html>
<html lang="en">
<head>
<meta charset="utf-8">
<title>Greywater Business Card</title>
<link rel="stylesheet" href="https://fonts.googleapis.com/css2?family=Didact+Gothic&display=swap">
<style>
  :root {
    --lime: #bfdc2c;
    --white: #ffffff;
    --grey-light: #767676;
    --grey-mid: #3a3a3a;
    --black: #000000;
    --font: "Didact Gothic", "Century Gothic", sans-serif;
  }
  html, body {
    margin: 0;
    padding: 0;
    width: 1200px;
    height: 790px;
    overflow: hidden;
    background: var(--black);
  }
  .card {
    position: relative;
    width: 1200px;
    height: 790px;
    overflow: hidden;
    font-family: var(--font);
    color: var(--white);
    background:
      radial-gradient(ellipse 900px 620px at 900px 60px, var(--grey-light) 0%, var(--grey-mid) 45%, var(--black) 85%),
      var(--black);
  }
  .card::before {
    content: "";
    position: absolute;
    inset: 0;
    background: linear-gradient(90deg, var(--black) 0%, rgba(0,0,0,0.55) 18%, rgba(0,0,0,0) 45%);
  }
  .brand {
    position: absolute;
    left: 0;
    top: 0;
    width: 1200px;
    height: 300px;
  }
  .brand-name {
    font-family: var(--font);
    fill: var(--lime);
    font-size: 215px;
  }
  .services {
    position: absolute;
    left: 96px;
    top: 282px;
    margin: 0;
    font-size: 35px;
    line-height: 1;
    white-space: nowrap;
  }
  .address {
    position: absolute;
    left: 810px;
    width: 395px;
    top: 330px;
    margin: 0;
    font-style: normal;
    text-align: center;
    font-size: 36px;
    line-height: 60px;
    white-space: nowrap;
  }
  .address span { display: block; }
  .contact {
    position: absolute;
    left: 44px;
    top: 630px;
    margin: 0;
    font-size: 36px;
    line-height: 62px;
    white-space: nowrap;
  }
  .contact span { display: block; }
</style>
</head>
<body>
  <main class="card">
    <svg class="brand" viewBox="0 0 1200 300" aria-label="Greywater">
      <text class="brand-name" x="92" y="240" textLength="1010" lengthAdjust="spacing">Greywater</text>
    </svg>
    <p class="services">Irish Horse Sales . Livery . Stud . Shows</p>
    <address class="address">
      <span>Mark Dabrowski</span>
      <span>Greywater Stud</span>
      <span>Birch Lodge</span>
      <span>Carrowmede Lane</span>
      <span>Thistlecombe</span>
      <span>Wendlowshire</span>
      <span>QX4 7JX</span>
    </address>
    <p class="contact">
      <span>Email. office@greywaterstud.co.uk</span>
      <span>Tel. 07482 936504</span>
    </p>
  </main>
</body>
</html>
```